Small property developments

I'm just starting out developing duplex homes on urban infill sites in the Brackwood City Council region of Brisbane. I need a business card to give to planners, engineers and builders. I was thinking of a logo that showed two homes under a single roof which is what a duplex is, but all good development and construction themes considered. Company name will be Marty Loft Developments.

```html
<!DOCTYPE html>
<html lang="en">
<head>
<meta charset="utf-8">
<title>Marty Loft Development – Business Card</title>
<link rel="stylesheet" href="https://fonts.googleapis.com/css2?family=Cabin:wght@600;700&family=PT+Sans+Narrow:wght@400;700&family=Open+Sans:wght@400;700&display=swap">
<style>
  :root {
    --page-bg: #ffffff;
    --ink: #111111;
    --green-deep: #1f8a35;
    --green-mid: #3aa63c;
    --green-light: #8cc63f;
    --brand-green: #3c9a32;
    --card-white: #ffffff;
    --frame-line: rgba(200, 235, 150, 0.75);
  }

  * { box-sizing: border-box; margin: 0; padding: 0; }

  html, body {
    width: 750px;
    height: 1200px;
    overflow: hidden;
    background: var(--page-bg);
  }

  .sheet {
    position: relative;
    width: 750px;
    height: 1200px;
  }

  .side-label {
    position: absolute;
    left: 0;
    width: 750px;
    text-align: center;
    font-family: "Open Sans", sans-serif;
    font-weight: 700;
    font-size: 33px;
    color: var(--ink);
  }
  .side-label--front { top: 160px; }
  .side-label--back  { top: 596px; }

  /* Front card */
  .card-front {
    position: absolute;
    left: 99px;
    top: 213px;
    width: 584px;
    height: 305px;
    background: var(--card-white);
    border: 2px solid var(--green-mid);
    display: flex;
  }

  .card-front__band {
    width: 150px;
    height: 100%;
    background: linear-gradient(90deg, var(--green-deep) 0%, var(--green-mid) 45%, var(--green-light) 100%);
    display: flex;
    align-items: center;
    justify-content: center;
  }

  .card-front__mark {
    font-family: "PT Sans Narrow", sans-serif;
    font-size: 50px;
    color: #ffffff;
    letter-spacing: -1px;
  }

  .card-front__body {
    position: relative;
    flex: 1;
  }

  .company-name {
    position: absolute;
    top: 30px;
    left: 0;
    right: 0;
    text-align: center;
    font-family: "Cabin", sans-serif;
    font-weight: 700;
    font-size: 27px;
    color: var(--brand-green);
    letter-spacing: 0.3px;
  }

  .company-slogan {
    position: absolute;
    top: 66px;
    left: 0;
    right: 0;
    text-align: center;
    font-family: "Cabin", sans-serif;
    font-weight: 600;
    font-style: italic;
    font-size: 17px;
    color: var(--brand-green);
  }

  .contact-list {
    position: absolute;
    left: 112px;
    top: 208px;
    list-style: none;
    font-family: "Open Sans", sans-serif;
    font-size: 13px;
    line-height: 17px;
    color: var(--brand-green);
  }

  /* Back card */
  .card-back {
    position: absolute;
    left: 85px;
    top: 660px;
    width: 580px;
    height: 310px;
    background: linear-gradient(120deg, var(--green-mid) 0%, var(--green-deep) 50%, #4fb043 100%);
    display: flex;
    flex-direction: column;
    align-items: center;
    justify-content: center;
  }

  .card-back__frame {
    position: absolute;
    inset: 30px 34px;
    border: 3px solid var(--frame-line);
    border-radius: 18px;
  }

  .card-back__mark {
    position: relative;
    font-family: "PT Sans Narrow", sans-serif;
    font-size: 104px;
    line-height: 1.22;
    color: #ffffff;
    letter-spacing: -2px;
  }

  .card-back__slogan {
    position: relative;
    font-family: "PT Sans Narrow", sans-serif;
    font-size: 36px;
    line-height: 1.1;
    color: #ffffff;
    margin-top: 0;
  }
</style>
</head>
<body>
<main class="sheet">
  <h2 class="side-label side-label--front">Front Side</h2>

  <section class="card-front" aria-label="Business card front">
    <div class="card-front__band">
      <span class="card-front__mark">Logo</span>
    </div>
    <div class="card-front__body">
      <h1 class="company-name">Marty Loft Development</h1>
      <p class="company-slogan">slogan slogan slogan</p>
      <ul class="contact-list">
        <li>phone###########</li>
        <li>Fax#######</li>
        <li>Add;-----------------</li>
        <li>www.martyloftdevelopment.com</li>
      </ul>
    </div>
  </section>

  <h2 class="side-label side-label--back">Back Side</h2>

  <section class="card-back" aria-label="Business card back">
    <div class="card-back__frame"></div>
    <span class="card-back__mark">Logo</span>
    <p class="card-back__slogan">slogan slogan slogan slogan</p>
  </section>
</main>
</body>
</html>
```